Business Card Design

www.bellwaterridge.com.au

Bellwater Ridge Bed and Breakfast
A unique property with spectacular views situated in a peaceful quiet court surrounded by other quality homes. Set back from the street, this wonderful residence has plenty of space. The huge paved driveway has tonnes of off street parking

Relax in the beautifully landscaped lawn area with mature trees. The stunning balcony & deck is an ideal place to sit & watch the spectacular sunsets through the tree tops. Just wonderful!

The self-contained Bed and Breakfast has its own separate entrance door and consists of a large lounge/ kitchenette with sink & a separate bedroom. The bathroom has a glass shower screen, toilet & vanity unit.
If you are looking for your own piece of paradise in an ideal established setting with plenty of room then you must stay at Bellwater ridge
This really is a slice of Heaven so come & stay!

- Established landscaped gardens & lawn areas
- paved driveway - loads of off street parking
- Splendid balcony with glorious views
- Close to shopping & transport

We welcome you to relax and unwind in the charm of our modern country feel bed and breakfast in the Northern Suburbs of Adelaide, offering privacy and relaxation, it is perfect for couples
This self-contained bed & breakfast will provide you with a “home away from home”, including breakfast provisions and all the comfort and modern conveniences you’d expect Bellwater Ridge is perfect whether you’re on a holiday visit to Adelaide or here for business.
Enjoy the many activities Adelaide has to offer, we are positioned in the Northern Suburbs for you to easily travel to the Adelaide Hills or Barossa Wine region.
Bellwater Ridge B & B is in a fantastic location for whatever you want to do on your visit to South Australia. Nestled within walking distance to the Cobbler Creek or visit our world renowned wine regions. Of course, we can help and point you in the right direction.

Shopping

14 Bellwater Court
Kelmont Heights SA 5192

Dennis & Maureen Pellham
0412 555 648 or 0413 555 927
www.bellwaterridge.com.au
dennis@bellwaterridge.com.au

```html
<!DOCTYPE html>
<html lang="en">
<head>
<meta charset="utf-8">
<title>Bellwater Ridge Business Card</title>
<link rel="stylesheet" href="https://fonts.googleapis.com/css2?family=Arimo:wght@400;700&display=swap">
<style>
  :root {
    --card-bg: #ffffff;
    --ink: #111111;
    --page-bg: #ffffff;
  }
  html, body {
    margin: 0;
    padding: 0;
    width: 1200px;
    height: 743px;
    overflow: hidden;
    background: var(--page-bg);
  }
  .card {
    position: relative;
    width: 1200px;
    height: 743px;
    background: var(--card-bg);
    color: var(--ink);
    font-family: "Arimo", Arial, sans-serif;
  }
  .brand-name {
    position: absolute;
    left: 58px;
    top: 120px;
    margin: 0;
    font-size: 86px;
    font-weight: 400;
    line-height: 1;
    letter-spacing: 0.01em;
    color: var(--ink);
  }
  .details {
    position: absolute;
    left: 60px;
    top: 362px;
    margin: 0;
    font-style: normal;
    font-size: 29px;
    line-height: 48px;
  }
  .phones {
    position: absolute;
    left: 915px;
    top: 458px;
    margin: 0;
    font-size: 29px;
    line-height: 48px;
  }
  .online {
    position: absolute;
    right: 72px;
    top: 584px;
    margin: 0;
    text-align: right;
    font-size: 29px;
    font-weight: 700;
    line-height: 48px;
    letter-spacing: 0.08em;
  }
  .details span,
  .phones span,
  .online span {
    display: block;
  }
</style>
</head>
<body>
  <main class="card">
    <h1 class="brand-name">Bellwater Ridge</h1>

    <address class="details">
      <span class="business">Bellwater Ridge Bed and Breakfast</span>
      <span class="hosts">Dennis &amp; Maureen Pellham</span>
      <span class="street">14 Bellwater Court</span>
      <span class="suburb">Kelmont Heights SA 5192</span>
    </address>

    <p class="phones">
      <span class="phone">0412 555 648</span>
      <span class="phone">0413 555 927</span>
    </p>

    <p class="online">
      <span class="website">www.bellwaterridge.com.au</span>
      <span class="email">dennis@bellwaterridge.com.au</span>
    </p>
  </main>
</body>
</html>
```